Law Firm Logo and Business Card Design

I need a logo and business card design for a law firm I just started. The law firm is named Law Office of Doreen K. Ashworth, LLC. The type of law I practice is Family Law, which includes divorce, custody, child support, alimony, property division, and the like. I would like to see designs that are unique and modern, yet sophisticated. I would also like to use the logo/design for my letterhead. I am not opposed to using some form of the scales of justice although I'd like something other than the typical, old fashioned scales of justice. I had considered a house made out of puzzle pieces with one puzzle piece pulled away from the others, with the logo text reading "Putting your life back together, one piece at a time." However, I don't want that particular design to look juvenile. I also would not be opposed to some form of my initials on the logo -- my initials are DKA. I am open to any other ideas you may have. I would like to see raised designs/lettering, and/or metallic finish. I like the colors black, white, gold, silver, and/or teal.

Industry/Entity Type

Law Firm

```html
<!DOCTYPE html>
<html lang="en">
<head>
<meta charset="utf-8">
<title>Law Office of Doreen K. Ashworth, LLC — Business Card</title>
<link rel="stylesheet" href="https://fonts.googleapis.com/css2?family=Noto+Sans:wght@400;600&display=swap">
<style>
  :root {
    --paper: #ffffff;
    --edge: #333333;
    --ink: #1b1b1b;
    --gold: #d7b36a;
    --white: #ffffff;
  }
  html, body {
    margin: 0;
    padding: 0;
    width: 1200px;
    height: 750px;
    overflow: hidden;
    background: var(--paper);
  }
  .canvas {
    position: relative;
    width: 1200px;
    height: 750px;
    box-sizing: border-box;
    border: 2px solid var(--edge);
    background: var(--paper);
    font-family: "Noto Sans", Arial, sans-serif;
    color: var(--ink);
  }
  .card-frame {
    position: absolute;
    left: 63px;
    top: 67px;
    width: 1073px;
    height: 616px;
    background: var(--ink);
  }
  .card-face {
    position: absolute;
    left: 105px;
    top: 107px;
    width: 989px;
    height: 534px;
    background: var(--gold);
  }
  .firm-name {
    position: absolute;
    left: 160px;
    top: 192px;
    width: 672px;
    margin: 0;
    text-align: center;
    font-weight: 600;
    font-size: 44px;
    line-height: 58px;
    letter-spacing: 0.2px;
  }
  .divider {
    position: absolute;
    left: 479px;
    top: 327px;
    width: 3px;
    height: 291px;
    background: var(--ink);
  }
  .address {
    position: absolute;
    left: 511px;
    top: 355px;
    margin: 0;
    font-style: normal;
    font-size: 29px;
    line-height: 38px;
    font-weight: 400;
  }
  .contact-list {
    position: absolute;
    left: 511px;
    top: 511px;
    margin: 0;
    padding: 0;
    list-style: none;
    font-size: 29px;
    line-height: 38px;
  }
  .contact-list li {
    display: flex;
    align-items: center;
    gap: 16px;
  }
  .contact-icon {
    width: 22px;
    height: 22px;
    flex: none;
  }
  .monogram {
    position: absolute;
    left: 184px;
    top: 470px;
    display: flex;
    align-items: center;
    gap: 16px;
    font-weight: 600;
    font-size: 52px;
    line-height: 1;
    color: var(--ink);
  }
  .monogram-dot {
    width: 40px;
    height: 40px;
    border-radius: 50%;
    border: 3px solid var(--white);
    box-sizing: border-box;
  }
</style>
</head>
<body>
  <div class="canvas">
    <div class="card-frame"></div>
    <div class="card-face"></div>

    <h1 class="firm-name">Law Office of<br>Doreen K. Ashworth, LLC.</h1>

    <div class="monogram" aria-label="DKA">
      <span class="monogram-dot"></span>
      <span>DKA</span>
    </div>

    <div class="divider"></div>

    <address class="address">
      2417 Harbor Point Rd.<br>
      Suite 140<br>
      Annapolis, MD 21403
    </address>

    <ul class="contact-list">
      <li>
        <svg class="contact-icon" viewBox="0 0 22 22" aria-hidden="true">
          <rect width="22" height="22" rx="4" fill="#1b1b1b"/>
          <path d="M7 5 L9 5 L10 8 L8.6 9.2 Q10 12.4 12.8 13.4 L14 12 L17 13 L17 15 Q16.5 17 14.5 17 Q6 15.5 5 7.5 Q5 5 7 5 Z" fill="#ffffff"/>
        </svg>
        <span>+443-555-0192</span>
      </li>
      <li>
        <svg class="contact-icon" viewBox="0 0 22 22" aria-hidden="true">
          <rect width="22" height="22" rx="4" fill="#1b1b1b"/>
          <rect x="3.5" y="6" width="15" height="10.5" fill="#ffffff"/>
          <path d="M3.5 6 L11 12 L18.5 6 M3.5 16.5 L9 11 M18.5 16.5 L13 11" fill="none" stroke="#1b1b1b" stroke-width="1.2"/>
        </svg>
        <span>doreen@ashworthfamilylaw.com</span>
      </li>
      <li>
        <svg class="contact-icon" viewBox="0 0 22 22" aria-hidden="true">
          <rect width="22" height="22" rx="4" fill="#1b1b1b"/>
          <g fill="none" stroke="#ffffff" stroke-width="1.1">
            <circle cx="11" cy="11" r="6.5"/>
            <ellipse cx="11" cy="11" rx="3" ry="6.5"/>
            <path d="M4.5 11 H17.5 M5.5 7.8 H16.5 M5.5 14.2 H16.5"/>
          </g>
        </svg>
        <span>www.ashworthfamilylaw.com</span>
      </li>
    </ul>
  </div>
</body>
</html>
```